Template for Pharmacy Daily Specials Campaign

We are an independent retail pharmacy serving to Los Angeles are for more than 25 years. we accept all major insurance plans and are launching our own discount generic medication program to help people save money. The program is cash only, pre-paid orders and free delivery with a minimum order of $40. We are trying to create a design that we can use for print Monthly Ads and Fliers. I have attached files with rough sketches and design ideas. The wording and layout are just ideas that we came up with and we are open to other suggestions.
Insured and Un-insured patients in the state of California. The largest clientele would be senior citizens and baby boomers
- the ad must state that enrollment is required to participate and fees are waived for new customers.
- Must be eye-catching and easy to understand/read.
- I have included files for our logo and we like to use shades of green that are a little darker
- would prefer the look of real life items
- prefer no animated designs

```html
<!DOCTYPE html>
<html lang="en">
<head>
<meta charset="utf-8">
<title>Corner Care Pharmacy – Club CCP Monthly Specials</title>
<link rel="stylesheet" href="https://fonts.googleapis.com/css2?family=Oswald:wght@300;400;500;600;700&display=swap">
<style>
  :root {
    --teal: #12b096;
    --teal-dark: #0e9a83;
    --sky: #9fd0f1;
    --sky-soft: #c7e4f7;
    --ink: #1d1d1d;
    --paper: #ffffff;
    --dots: #c9c9c9;
    --shelf-light: #f4f1ec;
    --shelf-mid: #e3ddd3;
    --shelf-warm: #e9c9b8;
  }
  * { box-sizing: border-box; margin: 0; padding: 0; }
  html, body { width: 883px; height: 1200px; overflow: hidden; background: var(--paper); }
  body { font-family: "Oswald", "Arial Narrow", sans-serif; color: var(--ink); }
  .flyer { position: relative; width: 883px; height: 1200px; background: var(--paper); overflow: hidden; }

  .top-band { position: absolute; left: 0; top: 0; width: 883px; height: 296px; background: var(--teal); }

  .hero-ring { position: absolute; left: 80px; top: 96px; width: 710px; height: 392px; border-radius: 50%; background: var(--sky); }
  .hero-gap { position: absolute; left: 90px; top: 106px; width: 690px; height: 372px; border-radius: 50%; background: var(--paper); }
  .hero-photo {
    position: absolute; left: 96px; top: 112px; width: 678px; height: 360px; border-radius: 50%;
    border: 4px solid var(--teal);
    background:
      radial-gradient(ellipse 22% 60% at 50% 85%, #ffffff 0%, #f7f8f9 55%, rgba(247,248,249,0) 100%),
      linear-gradient(90deg, var(--shelf-warm) 0%, var(--shelf-light) 30%, var(--shelf-mid) 50%, var(--shelf-light) 70%, #d9e6ee 100%);
  }

  .brand-tab { position: absolute; left: 312px; top: 0; width: 260px; height: 168px; background: var(--sky); border-radius: 0 0 14px 14px; }
  .brand-box {
    position: absolute; left: 322px; top: 10px; width: 240px; height: 148px;
    background: var(--paper); border-radius: 12px;
    display: flex; flex-direction: column; align-items: center; justify-content: center; gap: 6px;
  }
  .brand-row { display: flex; align-items: center; gap: 10px; }
  .brand-mark { width: 22px; height: 22px; border-radius: 50%; background: var(--sky); }
  .brand-name { font-weight: 600; font-size: 27px; line-height: 1.05; color: var(--teal); text-transform: uppercase; }
  .brand-tagline { font-size: 9px; color: var(--sky); letter-spacing: 0.5px; }

  .contact {
    position: absolute; top: 525px; height: 43px; border-radius: 22px; background: var(--sky);
    display: flex; align-items: center; gap: 12px; padding-left: 10px;
    font-size: 17px; font-weight: 400; color: var(--ink);
  }
  .contact-icon { width: 30px; height: 30px; border-radius: 50%; border: 2px solid var(--ink); display: flex; align-items: center; justify-content: center; }
  .contact-phone { left: 57px; width: 224px; }
  .contact-mail { left: 317px; width: 250px; }
  .contact-fax { left: 603px; width: 224px; }

  .offer-frame { position: absolute; left: 27px; top: 621px; width: 827px; height: 565px; border: 3px solid var(--teal); border-top: none; }
  .frame-top-left { position: absolute; left: 27px; top: 619px; width: 135px; height: 3px; background: var(--teal); }
  .frame-top-right { position: absolute; left: 722px; top: 619px; width: 132px; height: 3px; background: var(--teal); }

  .offer-title { position: absolute; left: 0; width: 883px; top: 588px; text-align: center; font-size: 56px; line-height: 66px; color: var(--teal); font-weight: 300; }
  .offer-title strong { font-weight: 700; }

  .offer-ribbon { position: absolute; left: 53px; top: 671px; width: 777px; height: 46px; }
  .offer-ribbon-text { position: absolute; left: 63px; top: 671px; width: 750px; height: 46px; display: flex; align-items: center; justify-content: center; font-size: 22px; font-weight: 500; letter-spacing: -0.4px; color: var(--ink); white-space: nowrap; }

  .month-label { position: absolute; left: 80px; top: 734px; font-size: 30px; line-height: 34px; font-weight: 500; color: var(--teal); }
  .month-date { position: absolute; left: 80px; top: 766px; font-size: 42px; line-height: 48px; font-weight: 700; color: var(--teal); }

  .membership {
    position: absolute; left: 356px; top: 744px; width: 469px; height: 50px; border: 2px dotted var(--teal); border-radius: 25px;
    display: flex; align-items: center; justify-content: center; gap: 8px; font-size: 22px; color: var(--ink);
  }
  .membership strong { color: var(--teal); font-weight: 600; }

  .choice-line { position: absolute; left: 0; width: 883px; top: 826px; text-align: center; font-size: 26px; font-weight: 400; color: var(--sky); }

  .deal { position: absolute; width: 190px; height: 139px; border: 2px dotted var(--dots); border-radius: 12px; }
  .deal-price {
    position: absolute; right: 2px; bottom: 8px; width: 52px; height: 27px; background: var(--teal); color: var(--paper);
    border-radius: 10px 0 0 10px; font-size: 19px; font-weight: 500; display: flex; align-items: center; justify-content: center;
  }
  .row-1 { top: 876px; }
  .row-2 { top: 1027px; height: 137px; }
  .col-1 { left: 44px; } .col-2 { left: 245px; } .col-3 { left: 446px; } .col-4 { left: 648px; }
</style>
</head>
<body>
<main class="flyer">
  <div class="top-band"></div>

  <div class="hero-ring"></div>
  <div class="hero-gap"></div>
  <div class="hero-photo" role="img" aria-label="Smiling pharmacist in a white coat standing in front of shelves of medicine boxes"></div>

  <div class="brand-tab"></div>
  <div class="brand-box">
    <div class="brand-row">
      <span class="brand-mark"></span>
      <span class="brand-name">Corner Care<br>Pharmacy</span>
    </div>
    <span class="brand-tagline">your family care pharmacy team</span>
  </div>

  <div class="contact contact-phone">
    <span class="contact-icon">
      <svg width="16" height="16" viewBox="0 0 24 24"><path d="M6.6 10.8a15 15 0 0 0 6.6 6.6l2.2-2.2a1 1 0 0 1 1-.25 11.4 11.4 0 0 0 3.6.57 1 1 0 0 1 1 1V20a1 1 0 0 1-1 1A17 17 0 0 1 3 4a1 1 0 0 1 1-1h3.5a1 1 0 0 1 1 1c0 1.25.2 2.450.57 3.6a1 1 0 0 1-.25 1z" fill="#1d1d1d"/></svg>
    </span>
    (555) 014-2230
  </div>
  <div class="contact contact-mail">
    <span class="contact-icon">
      <svg width="16" height="16" viewBox="0 0 24 24"><rect x="2" y="5" width="20" height="14" rx="2" fill="#1d1d1d"/><path d="M3 6l9 7 9-7" stroke="#9fd0f1" stroke-width="2" fill="none"/></svg>
    </span>
    hello@cornercarerx.com
  </div>
  <div class="contact contact-fax">
    <span class="contact-icon">
      <svg width="16" height="16" viewBox="0 0 24 24"><rect x="6" y="3" width="12" height="5" fill="#1d1d1d"/><rect x="2" y="9" width="20" height="9" rx="2" fill="#1d1d1d"/><rect x="6" y="14" width="12" height="7" fill="#1d1d1d" stroke="#9fd0f1" stroke-width="1.5"/></svg>
    </span>
    (555) 014-2231
  </div>

  <div class="offer-frame"></div>
  <div class="frame-top-left"></div>
  <div class="frame-top-right"></div>
  <h1 class="offer-title">INTRODUCING <strong>CLUB CCP</strong></h1>

  <svg class="offer-ribbon" viewBox="0 0 777 46" width="777" height="46" aria-hidden="true">
    <polygon points="0,0 759,0 777,23 759,46 0,46 14,23" fill="#9fd0f1"/>
  </svg>
  <p class="offer-ribbon-text">100’S OF GENERIC MEDICINES FOR AS LITTLE AS $10 FOR A 3 MONTH SUPPLY</p>

  <p class="month-label">MONTHLY SPECIALS</p>
  <p class="month-date">AUGUST 2018</p>

  <p class="membership">Membership Required – <strong>Free Enrollment</strong></p>

  <p class="choice-line">YOUR CHOICE 10$ EACH</p>

  <div class="deal row-1 col-1"><span class="deal-price">10$</span></div>
  <div class="deal row-1 col-2"><span class="deal-price">10$</span></div>
  <div class="deal row-1 col-3"><span class="deal-price">10$</span></div>
  <div class="deal row-1 col-4"><span class="deal-price">10$</span></div>
  <div class="deal row-2 col-1"><span class="deal-price">10$</span></div>
  <div class="deal row-2 col-2"><span class="deal-price">10$</span></div>
  <div class="deal row-2 col-3"><span class="deal-price">10$</span></div>
  <div class="deal row-2 col-4"><span class="deal-price">10$</span></div>
</main>
</body>
</html>
```